Wall art for an Investments Lab at a college

Wall art for inside a new investments lab. A photo of the lab is attached. The wall art will go on the wall in the back right (pictured). It is currently white and the adjacent walls are white. The accent wall in the room is blue (summer nights). A copy of our color palette for environmental design is also attached. The tag line should be INVESTING IN THE FUTURE.

Target Market(s)

College students

Industry/Entity Type

Finance

Requirements
Must have
• Incorporate colors from palette

```html
<!DOCTYPE html>
<html lang="en">
<head>
<meta charset="utf-8">
<title>Investing in the Future — Investments Lab Wall Art</title>
<link rel="stylesheet" href="https://fonts.googleapis.com/css2?family=Allerta+Stencil&display=swap">
<style>
  :root {
    --steel-blue: #5488a3;
    --summer-night: #1a5674;
    --mid-teal: #336f8c;
    --panel-blue: #3f7390;
    --frost: #ffffff;
    --aqua-glow: #4ef0f5;
    --pale-cyan: #c9f7fb;
  }
  html, body {
    margin: 0;
    padding: 0;
    width: 1200px;
    height: 1033px;
    overflow: hidden;
    background: var(--summer-night);
  }
  .wall-art {
    position: relative;
    width: 1200px;
    height: 1033px;
    overflow: hidden;
    background: linear-gradient(90deg, var(--steel-blue) 0%, var(--mid-teal) 55%, var(--summer-night) 100%);
  }
  .mandala-field {
    position: absolute;
    inset: 0;
    width: 1200px;
    height: 1033px;
  }
  .tagline-panel {
    position: absolute;
    left: 80px;
    top: 443px;
    width: 998px;
    height: 137px;
    box-sizing: border-box;
    border: 7px solid var(--frost);
    background: linear-gradient(90deg, #44799a 0%, var(--panel-blue) 50%, #2a6583 100%);
    display: flex;
    align-items: center;
    justify-content: center;
  }
  .tagline {
    margin: 0;
    font-family: "Allerta Stencil", sans-serif;
    font-weight: 400;
    font-size: 60px;
    letter-spacing: 5px;
    line-height: 1;
    color: var(--frost);
    white-space: nowrap;
    padding-top: 6px;
  }
</style>
</head>
<body>
  <main class="wall-art">
    <svg class="mandala-field" viewBox="0 0 1200 1033" role="img" aria-label="Large ornate mandala of white and aqua floral petals, leaves and vines radiating from the centre across the whole wall">
      <defs>
        <linearGradient id="mandala-tone" x1="0" y1="0" x2="1" y2="0">
          <stop offset="0" stop-color="var(--frost)"/>
          <stop offset="0.6" stop-color="var(--pale-cyan)"/>
          <stop offset="1" stop-color="var(--aqua-glow)"/>
        </linearGradient>
        <radialGradient id="mandala-soft" cx="0.5" cy="0.5" r="0.5">
          <stop offset="0" stop-color="#000" stop-opacity="0"/>
          <stop offset="0.35" stop-color="#fff" stop-opacity="0.45"/>
          <stop offset="0.7" stop-color="#fff" stop-opacity="0.3"/>
          <stop offset="0.95" stop-color="#fff" stop-opacity="0.38"/>
          <stop offset="1" stop-color="#fff" stop-opacity="0"/>
        </radialGradient>
        <mask id="mandala-mask">
          <circle cx="580" cy="535" r="640" fill="url(#mandala-soft)"/>
        </mask>
      </defs>
      <rect width="1200" height="1033" fill="url(#mandala-tone)" mask="url(#mandala-mask)"/>
    </svg>
    <div class="tagline-panel">
      <h1 class="tagline">INVESTING IN THE FUTURE.</h1>
    </div>
  </main>
</body>
</html>
```